Natural, organic, vegan-friendly nutritious food supplements

We need packaging design for a new nutritious food supplement to be launched. The products are organic, natural, with no additives, lactose-free, gluten-free, vegan-friendly, etc. The product is a powder that comes in 40g sachets (need sachet design) which are then put into a box (need box design).

More details in the included zip file. Please do not hesitate to contact us for more information if needed.

Target Market(s)

Everyone interested in healthy food.

Requirements
Must have
• Vibrant colours, must be easy to read and easy to recognise on a shelf.
Natural colours.

```html
<!DOCTYPE html>
<html lang="en">
<head>
<meta charset="utf-8">
<title>Verda sachet range</title>
<link href="https://fonts.googleapis.com/css2?family=Playfair+Display:wght@400;700&family=Open+Sans:wght@400;600;700&display=swap" rel="stylesheet">
<style>
:root{
  --bg:#e6e8ea;
  --paper:#ffffff;
  --ink:#3a3a3a;
  --muted:#6b6b6b;
  --raspberry:#c8161d;
  --chocolate:#8d5f4b;
  --coconut:#efe4c2;
  --coconut-ink:#a87450;
  --table-green:#8cc63f;
}
*{box-sizing:border-box;margin:0;padding:0}
html,body{width:1200px;height:1200px;overflow:hidden}
body{background:var(--bg);font-family:"Open Sans",sans-serif;color:var(--ink);position:relative}
.sachet{position:absolute;width:320px;height:448px;background:var(--paper);overflow:hidden;box-shadow:0 2px 6px rgba(0,0,0,.12)}
.flavour-raspberry{--accent:var(--raspberry);--accent-ink:var(--raspberry);--image:#e0485f;--image2:#f3a8b6}
.flavour-chocolate{--accent:var(--chocolate);--accent-ink:#6e4a3a;--image:#5a3a2c;--image2:#d9c7b8}
.flavour-coconut{--accent:var(--coconut);--accent-ink:var(--coconut-ink);--image:#6f8f3f;--image2:#f3d36a}
.crimp{position:absolute;left:0;right:0;height:12px;background:repeating-linear-gradient(90deg,rgba(0,0,0,.05) 0 2px,transparent 2px 5px)}
.crimp.top{top:0}
.base-stripe{position:absolute;left:0;right:0;bottom:0;height:13px;background:var(--accent)}
.wave{position:absolute;left:0;top:0}
.wave-fill{fill:var(--accent)}
.wave-line{fill:none;stroke:var(--accent);stroke-width:2}
.brand{position:absolute;left:167px;top:75px;width:80px;height:80px;border-radius:50%;border:1.5px solid #333;background:var(--paper);display:flex;align-items:center;justify-content:center;font-family:"Playfair Display",serif;font-size:17px;color:#333}
.front-title{position:absolute;left:0;right:0;top:181px;text-align:center;font-family:"Playfair Display",serif;font-weight:400;font-size:20px;color:var(--accent-ink);letter-spacing:-.4px}
.front-sub{position:absolute;left:0;right:0;top:206px;text-align:center;font-family:"Playfair Display",serif;font-size:14px;color:var(--accent-ink);letter-spacing:.2px}
.flavour-chocolate .front-sub,.flavour-coconut .front-sub{font-size:11px;letter-spacing:1px}
.flavour-chocolate .front-title{color:#4a3a33}
.front-desc{position:absolute;left:22px;right:22px;top:238px;text-align:center;font-size:6.5px;line-height:1.35;color:var(--ink)}
.hero-image{position:absolute;left:60px;top:280px;width:200px;height:100px;border-radius:45%;background:radial-gradient(circle at 45% 50%,var(--image) 0 45%,var(--image2) 70%,transparent 72%)}
.net-weight{position:absolute;left:0;right:0;top:412px;text-align:center;font-size:8px;font-weight:700;color:var(--accent-ink)}
.flavour-chocolate .net-weight,.flavour-coconut .net-weight{color:#555}
.back-pill{position:absolute;left:50px;top:50px;width:216px;height:26px;border-radius:13px;background:var(--accent);color:#fff;font-size:13px;letter-spacing:1px;display:flex;align-items:center;justify-content:center}
.flavour-coconut .back-pill{color:var(--coconut-ink)}
.info{position:absolute;left:36px;width:110px;font-size:5.5px;line-height:1.35}
.info b{font-style:italic;font-weight:700;font-size:6px}
.prep{top:95px}
.ingredients{top:190px}
.steps{position:absolute;left:36px;top:132px;display:flex;gap:12px}
.step{width:20px;text-align:center;font-size:3.5px;font-style:italic}
.step svg{display:block;margin:0 auto 3px}
.certs{position:absolute;left:36px;top:270px;display:flex;gap:4px}
.certs span{width:13px;height:13px;border-radius:50%;border:1.5px solid #333}
.certs span.eu{border-radius:0;border:none;background:var(--table-green);width:16px;height:11px}
.nutrition{position:absolute;left:148px;top:92px;width:138px;border:1px solid #333;font-size:4px;line-height:6.8px;border-collapse:collapse}
.nutrition th{background:var(--table-green);font-weight:600;text-align:center}
.nutrition td{border-top:.5px solid #999;padding:0 2px}
.nutrition td+td{text-align:center}
.nutrition .section td{background:var(--table-green);font-weight:600}
.splash-image{position:absolute;left:26px;top:290px;width:170px;height:140px;background:radial-gradient(ellipse at 40% 45%,var(--image2),transparent 68%)}
.side-image{position:absolute;left:188px;top:296px;width:98px;height:62px;border-radius:40%;background:radial-gradient(circle,var(--image) 0 40%,transparent 70%)}
.back-meta{position:absolute;right:32px;top:380px;text-align:right;font-size:7.5px;line-height:16px;color:#222}
.back-meta .flavour{font-size:11px;letter-spacing:1.2px;color:var(--accent-ink)}
.flavour-chocolate .back-meta .flavour{color:#333}
.flavour-coconut .back-meta .flavour{color:#555}
</style>
</head>
<body>

<section class="sachet flavour-raspberry" style="left:63px;top:107px">
  <div class="crimp top"></div>
  <svg class="wave" width="320" height="160" viewBox="0 0 320 160"><path class="wave-fill" d="M0 0H320V55C230 60 130 95 0 135Z"/><path class="wave-line" d="M0 148C110 110 210 75 320 70"/></svg>
  <div class="brand">VERDA</div>
  <h1 class="front-title">RED AS CAN BE</h1>
  <p class="front-sub">RASPBERRY FLAVOUR</p>
  <p class="front-desc">Having run out of cacao powder, we mixed coconut and added some vanilla and boom, shakalaka! Just like the older brother chocolate and coconut, this one is also very good in terms of exercise in general</p>
  <div class="hero-image" role="img" aria-label="Fresh raspberries with mint leaves"></div>
  <p class="net-weight">NET WEIGHT: 40G</p>
  <div class="base-stripe"></div>
</section>

<section class="sachet flavour-chocolate" style="left:450px;top:107px">
  <div class="crimp top"></div>
  <svg class="wave" width="320" height="160" viewBox="0 0 320 160"><path class="wave-fill" d="M0 0H320V55C230 60 130 95 0 135Z"/><path class="wave-line" d="M0 148C110 110 210 75 320 70"/></svg>
  <div class="brand">VERDA</div>
  <h1 class="front-title">VELVET MIDNIGHT</h1>
  <p class="front-sub">CHOCOLATE &amp; COCONUT FLAVOUR</p>
  <p class="front-desc">Developed as something that everyone would like. Velvet Midnight is very balanced in terms of fat, carbohydrates and protein. Very good pre or post-workout drink, it is very much geared towards exercise.</p>
  <div class="hero-image" role="img" aria-label="Split coconut with chunks of dark chocolate"></div>
  <p class="net-weight">NET WEIGHT: 40G</p>
  <div class="base-stripe"></div>
</section>

<section class="sachet flavour-coconut" style="left:836px;top:107px">
  <div class="crimp top"></div>
  <svg class="wave" width="320" height="160" viewBox="0 0 320 160"><path class="wave-fill" d="M0 0H320V55C230 60 130 95 0 135Z"/><path class="wave-line" style="stroke:var(--coconut-ink)" d="M0 148C110 110 210 75 320 70"/></svg>
  <div class="brand">VERDA</div>
  <h1 class="front-title">NUTTY FOR YOU</h1>
  <p class="front-sub">COCONUT &amp; VANILLA FLAVOUR</p>
  <p class="front-desc">More delicate flavour profile but with a hint of sourness.<br>Easy to drink and nice in flavour</p>
  <div class="hero-image" role="img" aria-label="Coconut halves with vanilla flowers and leaves"></div>
  <p class="net-weight">NET WEIGHT: 40G</p>
  <div class="base-stripe"></div>
</section>

<section class="sachet flavour-raspberry" style="left:63px;top:615px">
  <div class="crimp top"></div>
  <div class="back-pill">RED AS CAN BE</div>
  <p class="info prep"><b>Preparation:</b> shake the contents with 200ml of your preferred liquid (water, milk, oat milk, rice milk, almond milk, etc.)</p>
  <div class="steps">
    <div class="step"><svg width="14" height="20" viewBox="0 0 14 20"><rect x="1" y="6" width="12" height="13" rx="2" fill="#222"/><rect x="3" y="1" width="8" height="4" fill="#222"/></svg>pour sachet</div>
    <div class="step"><svg width="14" height="20" viewBox="0 0 14 20"><rect x="1" y="6" width="12" height="13" rx="2" fill="#222"/><rect x="3" y="1" width="8" height="4" fill="#222"/></svg>add liquid</div>
    <div class="step"><svg width="14" height="20" viewBox="0 0 14 20"><rect x="1" y="6" width="12" height="13" rx="2" fill="#222"/><rect x="3" y="1" width="8" height="4" fill="#222"/></svg>drink</div>
  </div>
  <p class="info ingredients"><b>Ingredients:</b> organic oatmeal flour, organic freeze-dried raspberry powder, organic rice protein 80%, organic lucuma powder, organic chia seeds powder, organic flaxseed powder, organic apple powder, organic maca powder, organic mushroom extract.</p>
  <div class="certs"><span></span><span></span><span></span><span></span><span class="eu"></span></div>
  <table class="nutrition">
    <tr><th>Nutrition</th><th>Per 100g</th><th>Per serving</th></tr>
    <tr><td>Energy kcal</td><td>386</td><td>154</td></tr><tr><td>Carbohydrate</td><td>49.0</td><td>19.6</td></tr><tr><td>Fat</td><td>9.0</td><td>3.6</td></tr><tr><td>Sugars</td><td>8.7</td><td>3.5</td></tr><tr><td>Fibre</td><td>10.6</td><td>4.2</td></tr><tr><td>Protein</td><td>24.0</td><td>9.6</td></tr><tr><td>Salt</td><td>0.1</td><td>0.0</td></tr>
    <tr class="section"><td>Vitamins</td><td></td><td></td></tr>
    <tr><td>B1 mg</td><td>0.3</td><td>0.1</td></tr><tr><td>B2 mg</td><td>0.2</td><td>0.1</td></tr><tr><td>B3 mg</td><td>2.5</td><td>1.0</td></tr><tr><td>B6 mg</td><td>0.4</td><td>0.2</td></tr><tr><td>C mg</td><td>12</td><td>4.8</td></tr><tr><td>E mg</td><td>1.5</td><td>0.6</td></tr>
    <tr class="section"><td>Minerals</td><td></td><td></td></tr>
    <tr><td>Calcium mg</td><td>145</td><td>58</td></tr><tr><td>Iron mg</td><td>6.2</td><td>2.5</td></tr><tr><td>Magnesium mg</td><td>172</td><td>69</td></tr><tr><td>Zinc mg</td><td>3.1</td><td>1.2</td></tr><tr><td>Potassium mg</td><td>610</td><td>244</td></tr><tr><td>Selenium µg</td><td>8.0</td><td>3.2</td></tr>
  </table>
  <div class="splash-image" role="img" aria-label="Pink raspberry shake splashing"></div>
  <div class="side-image" role="img" aria-label="Raspberries with mint leaves"></div>
  <div class="back-meta">Produced in Denmark<br>New Nutritious Food Supplement<br><span class="flavour">RASPBERRY FLAVOUR</span></div>
  <div class="base-stripe"></div>
</section>

<section class="sachet flavour-chocolate" style="left:450px;top:615px">
  <div class="crimp top"></div>
  <div class="back-pill">VELVET MIDNIGHT</div>
  <p class="info prep"><b>Preparation:</b> shake the contents with 200ml of your preferred liquid (water, milk, oat milk, rice milk, almond milk, etc.)</p>
  <div class="steps">
    <div class="step"><svg width="14" height="20" viewBox="0 0 14 20"><rect x="1" y="6" width="12" height="13" rx="2" fill="#222"/><rect x="3" y="1" width="8" height="4" fill="#222"/></svg>pour sachet</div>
    <div class="step"><svg width="14" height="20" viewBox="0 0 14 20"><rect x="1" y="6" width="12" height="13" rx="2" fill="#222"/><rect x="3" y="1" width="8" height="4" fill="#222"/></svg>add liquid</div>
    <div class="step"><svg width="14" height="20" viewBox="0 0 14 20"><rect x="1" y="6" width="12" height="13" rx="2" fill="#222"/><rect x="3" y="1" width="8" height="4" fill="#222"/></svg>drink</div>
  </div>
  <p class="info ingredients"><b>Ingredients:</b> Organic coconut milk powder, organic lucuma powder, organic cacao powder, organic oatmeal flour, organic chia seeds powder, organic flaxseed powder, organic rice protein 80%, organic maca powder, organic mushroom extract.</p>
  <div class="certs"><span></span><span></span><span></span><span></span><span class="eu"></span></div>
  <table class="nutrition">
    <tr><th>Nutrition</th><th>Per 100g</th><th>Per serving</th></tr>
    <tr><td>Energy kcal</td><td>412</td><td>165</td></tr><tr><td>Carbohydrate</td><td>42.0</td><td>16.8</td></tr><tr><td>Fat</td><td>16.2</td><td>6.5</td></tr><tr><td>Sugars</td><td>7.9</td><td>3.2</td></tr><tr><td>Fibre</td><td>11.4</td><td>4.6</td></tr><tr><td>Protein</td><td>22.5</td><td>9.0</td></tr><tr><td>Salt</td><td>0.1</td><td>0.0</td></tr>
    <tr class="section"><td>Vitamins</td><td></td><td></td></tr>
    <tr><td>B1 mg</td><td>0.3</td><td>0.1</td></tr><tr><td>B2 mg</td><td>0.2</td><td>0.1</td></tr><tr><td>B3 mg</td><td>2.2</td><td>0.9</td></tr><tr><td>B6 mg</td><td>0.4</td><td>0.2</td></tr><tr><td>C mg</td><td>4.0</td><td>1.6</td></tr><tr><td>E mg</td><td>1.1</td><td>0.4</td></tr>
    <tr class="section"><td>Minerals</td><td></td><td></td></tr>
    <tr><td>Calcium mg</td><td>128</td><td>51</td></tr><tr><td>Iron mg</td><td>7.4</td><td>3.0</td></tr><tr><td>Magnesium mg</td><td>210</td><td>84</td></tr><tr><td>Zinc mg</td><td>3.5</td><td>1.4</td></tr><tr><td>Potassium mg</td><td>690</td><td>276</td></tr><tr><td>Selenium µg</td><td>7.2</td><td>2.9</td></tr>
  </table>
  <div class="splash-image" role="img" aria-label="Chocolate shake splashing"></div>
  <div class="side-image" role="img" aria-label="Coconut and dark chocolate pieces"></div>
  <div class="back-meta">Produced in Denmark<br>New Nutritious Food Supplement<br><span class="flavour">CHOCOLATE &amp; COCONUT</span></div>
  <div class="base-stripe"></div>
</section>

<section class="sachet flavour-coconut" style="left:836px;top:615px">
  <div class="crimp top"></div>
  <div class="back-pill">NUTTY FOR YOU</div>
  <p class="info prep"><b>Preparation:</b> shake the contents with 200ml of your preferred liquid (water, milk, oat milk, rice milk, almond milk, etc.)</p>
  <div class="steps">
    <div class="step"><svg width="14" height="20" viewBox="0 0 14 20"><rect x="1" y="6" width="12" height="13" rx="2" fill="#222"/><rect x="3" y="1" width="8" height="4" fill="#222"/></svg>pour sachet</div>
    <div class="step"><svg width="14" height="20" viewBox="0 0 14 20"><rect x="1" y="6" width="12" height="13" rx="2" fill="#222"/><rect x="3" y="1" width="8" height="4" fill="#222"/></svg>add liquid</div>
    <div class="step"><svg width="14" height="20" viewBox="0 0 14 20"><rect x="1" y="6" width="12" height="13" rx="2" fill="#222"/><rect x="3" y="1" width="8" height="4" fill="#222"/></svg>drink</div>
  </div>
  <p class="info ingredients"><b>Ingredients:</b> Organic coconut milk powder, organic oatmeal flour, organic lucuma powder, organic chia seeds powder, organic flaxseed powder, organic rice protein 80%, organic mushroom extract, organic vanilla extract.</p>
  <div class="certs"><span></span><span></span><span></span><span></span><span class="eu"></span></div>
  <table class="nutrition">
    <tr><th>Nutrition</th><th>Per 100g</th><th>Per serving</th></tr>
    <tr><td>Energy kcal</td><td>405</td><td>162</td></tr><tr><td>Carbohydrate</td><td>44.8</td><td>17.9</td></tr><tr><td>Fat</td><td>15.0</td><td>6.0</td></tr><tr><td>Sugars</td><td>8.1</td><td>3.2</td></tr><tr><td>Fibre</td><td>10.2</td><td>4.1</td></tr><tr><td>Protein</td><td>21.8</td><td>8.7</td></tr><tr><td>Salt</td><td>0.1</td><td>0.0</td></tr>
    <tr class="section"><td>Vitamins</td><td></td><td></td></tr>
    <tr><td>B1 mg</td><td>0.3</td><td>0.1</td></tr><tr><td>B2 mg</td><td>0.2</td><td>0.1</td></tr><tr><td>B3 mg</td><td>2.0</td><td>0.8</td></tr><tr><td>B6 mg</td><td>0.3</td><td>0.1</td></tr><tr><td>C mg</td><td>3.2</td><td>1.3</td></tr><tr><td>E mg</td><td>1.0</td><td>0.4</td></tr>
    <tr class="section"><td>Minerals</td><td></td><td></td></tr>
    <tr><td>Calcium mg</td><td>120</td><td>48</td></tr><tr><td>Iron mg</td><td>5.8</td><td>2.3</td></tr><tr><td>Magnesium mg</td><td>165</td><td>66</td></tr><tr><td>Zinc mg</td><td>2.9</td><td>1.2</td></tr><tr><td>Potassium mg</td><td>580</td><td>232</td></tr><tr><td>Selenium µg</td><td>6.8</td><td>2.7</td></tr>
  </table>
  <div class="splash-image" role="img" aria-label="Creamy yellow vanilla shake splashing"></div>
  <div class="side-image" role="img" aria-label="Coconut with vanilla flowers and leaves"></div>
  <div class="back-meta">Produced in Denmark<br>New Nutritious Food Supplement<br><span class="flavour">COCONUT &amp; VANILLA</span></div>
  <div class="base-stripe"></div>
</section>

</body>
</html>
```